Honolulu based car rental and retail shop needs a business card

We need a card design for an established company in Honolulu called Reefline Motor Traders. We rent cars mainly to tourists and visitors through an app called Zavi. (Zavi is not ours)- We also retail cars at the same location... The card should communicate a modern island/tropical feel. I have my website in limbo with a old "friend".. So for now we'll omit the web info until I can regain control of the site. We can also use a small version of the Zavi logo to go with the account info.

Target Market(s)

Walk in and client meetings

Contact Information for Business Card

I need to have address, ph #, email, and I'd love to have a highlighted section with my Zavi act. info.

Logo Text

Reefline Motor Traders

Font styles to use
Serif

Colors
3276b5
ffffff
faa54b
fcca95
eaf1f7

Requirements
Must have
• Derek Munroe
• email: derek@reeflinemotorhire.example
• Ph# 808-555-0143
• Address: 1417 Keawe Ln. Honolulu, Hi 96801
• Zavi: https://zavi.example/en-us/drivers/5193072
Nice to have
• To Rent: https://zavi.example/en-us/drivers/5193072
• To Buy: 1417 Keawe Ln. Honolulu Hi 96801
• Maybe some suggestions here would be nice too! Maybe double sided?

```html
<!DOCTYPE html>
<html lang="en">
<head>
<meta charset="utf-8">
<title>Reefline Motor Traders – Business Card</title>
<link rel="stylesheet" href="https://fonts.googleapis.com/css2?family=Roboto:wght@400;700&display=swap">
<style>
  :root {
    --backdrop: #e4e5e6;
    --navy: #1a4579;
    --card-white: #f4f4f4;
    --lime: #a9bf3a;
    --maroon: #6b1a1a;
    --ink: #2b2b2b;
    --white: #ffffff;
  }
  * { margin: 0; padding: 0; box-sizing: border-box; }
  html, body {
    width: 1200px; height: 960px; overflow: hidden;
    background: var(--backdrop);
    font-family: "Roboto", Arial, sans-serif;
  }
  .canvas { position: relative; width: 1200px; height: 960px; }
  .card {
    position: absolute; top: 173px;
    width: 350px; height: 612px;
    border-radius: 22px; overflow: hidden;
  }
  .card--front { left: 223px; background: var(--navy); }
  .card--back { left: 627px; background: var(--card-white); }

  .brand-name {
    position: absolute; left: 0; width: 100%;
    text-align: center; font-weight: 700;
    line-height: 1.05; letter-spacing: 0.5px;
  }
  .card--front .brand-name { top: 225px; font-size: 40px; color: var(--white); }
  .card--back .brand-name { top: 90px; font-size: 38px; color: var(--navy); }

  .holder-name {
    position: absolute; top: 290px; width: 100%;
    text-align: center; font-size: 22px; font-weight: 700; color: var(--navy);
  }
  .contact-block {
    position: absolute; width: 100%; text-align: center;
    font-size: 16px; line-height: 21px; color: var(--ink);
  }
  .contact-block--address { top: 345px; }
  .contact-block--reach { top: 423px; }
  .icon-row { display: flex; justify-content: center; gap: 8px; margin-bottom: 6px; }
  .icon-row svg { width: 20px; height: 20px; display: block; }

  .rental-band { position: absolute; left: 0; bottom: 0; width: 350px; height: 100px; }
  .rental-band svg { position: absolute; inset: 0; }
  .partner-name {
    position: absolute; top: 0; width: 100%; text-align: center;
    font-size: 20px; font-weight: 700; color: var(--ink); letter-spacing: 1px;
  }
  .rental-link {
    position: absolute; top: 64px; width: 100%; text-align: center;
    font-size: 15px; color: var(--white);
  }
</style>
</head>
<body>
<div class="canvas">
  <section class="card card--front">
    <div class="brand-name">Reefline<br>Motor Traders</div>
  </section>

  <section class="card card--back">
    <div class="brand-name">Reefline<br>Motor Traders</div>

    <h1 class="holder-name">Derek Munroe</h1>

    <div class="contact-block contact-block--address">
      <div class="icon-row">
        <svg viewBox="0 0 20 20" aria-hidden="true">
          <circle cx="10" cy="10" r="10" fill="var(--maroon)"/>
          <path d="M10 4a4 4 0 0 0-4 4c0 3 4 8 4 8s4-5 4-8a4 4 0 0 0-4-4z" fill="#fff"/>
          <circle cx="10" cy="8" r="1.6" fill="var(--maroon)"/>
        </svg>
      </div>
      <p>1417 Keawe Ln.</p>
      <p>Honolulu, Hi 96801</p>
    </div>

    <div class="contact-block contact-block--reach">
      <div class="icon-row">
        <svg viewBox="0 0 20 20" aria-hidden="true">
          <circle cx="10" cy="10" r="10" fill="var(--maroon)"/>
          <path d="M6.5 5l2 .2.8 2.4-1.2 1a7 7 0 0 0 3.3 3.3l1-1.2 2.4.8.2 2c-.3.6-1 1-1.7 1A9 9 0 0 1 5.5 6.7c0-.7.4-1.4 1-1.7z" fill="#fff"/>
        </svg>
        <svg viewBox="0 0 20 20" aria-hidden="true">
          <circle cx="10" cy="10" r="10" fill="var(--maroon)"/>
          <rect x="5" y="6.5" width="10" height="7" fill="none" stroke="#fff" stroke-width="1.3"/>
          <path d="M5 6.5l5 4 5-4" fill="none" stroke="#fff" stroke-width="1.3"/>
        </svg>
      </div>
      <p>808-555-0143</p>
      <p>derek@reeflinemotorhire.example</p>
    </div>

    <div class="rental-band">
      <svg viewBox="0 0 350 100" aria-hidden="true">
        <path d="M0 44 Q175 5 350 44 L350 52 Q175 14 0 52 Z" fill="var(--lime)"/>
        <path d="M0 52 Q175 14 350 52 L350 100 L0 100 Z" fill="var(--navy)"/>
        <path d="M0 52 Q175 14 350 52" fill="none" stroke="#fff" stroke-width="2"/>
      </svg>
      <div class="partner-name">Zavi</div>
      <p class="rental-link">zavi.example/en-us/drivers/5193072 (Rent)</p>
    </div>
  </section>
</div>
</body>
</html>
```